URGENT Christmas Greeting Card for IT Company

We URGENTLY need a Christmas Card for our clients. We are an IT Company that resell softwares from developers. We need the final design for Friday at the latest.

We are looking for a creative, yet elegant christmas card to give to our clients along with a gift. Please use our logo and the same color scheme.

Industry/Entity Type

It Company

Requirements
Must have
• Must have the logo and the colors of christmas and the company.
Nice to have
• I would like to see creative yet elegant designs, its a christmas card that a company is giving to its clients. It would be nice to see a modern, serious and elegant designs.

```html
<!DOCTYPE html>
<html lang="en">
<head>
<meta charset="UTF-8">
<title>Holiday Greeting Card</title>
<link href="https://fonts.googleapis.com/css2?family=Open+Sans:wght@300;400;700&display=swap" rel="stylesheet">
<style>
  :root {
    --paper: #ffffff;
    --festive-red: #e63430;
    --tree-blush: #f9d6d6;
    --tree-blush-soft: #fce7e7;
    --ink: #2b2b2b;
  }
  * { margin: 0; padding: 0; box-sizing: border-box; }
  html, body {
    width: 848px;
    height: 1200px;
    overflow: hidden;
    background: var(--paper);
  }
  .card {
    position: relative;
    width: 848px;
    height: 1200px;
    background: var(--paper);
    font-family: "Open Sans", Arial, sans-serif;
  }
  .tree-art {
    position: absolute;
    left: 390px;
    top: 384px;
    width: 72px;
    height: 126px;
  }
  .greeting {
    position: absolute;
    left: 0;
    top: 540px;
    width: 100%;
    text-align: center;
    color: var(--festive-red);
    font-weight: 300;
    font-size: 31px;
    line-height: 38px;
    text-transform: uppercase;
    letter-spacing: 0.2px;
  }
  .brand {
    position: absolute;
    left: 0;
    top: 1068px;
    width: 100%;
    text-align: center;
  }
  .brand-name {
    display: block;
    color: var(--ink);
    font-weight: 700;
    font-size: 28px;
    line-height: 30px;
    letter-spacing: -0.5px;
  }
  .brand-tagline {
    display: block;
    margin-top: 2px;
    color: var(--ink);
    font-weight: 400;
    font-size: 9px;
    letter-spacing: 0.3px;
    text-transform: uppercase;
  }
</style>
</head>
<body>
  <main class="card">
    <svg class="tree-art" viewBox="0 0 72 126" role="img" aria-label="Minimal striped Christmas tree illustration in pale pink">
      <defs>
        <linearGradient id="treeFill" x1="0" y1="0" x2="0" y2="1">
          <stop offset="0" stop-color="var(--tree-blush-soft)"/>
          <stop offset="1" stop-color="var(--tree-blush)"/>
        </linearGradient>
      </defs>
      <rect x="0" y="0" width="72" height="126" fill="url(#treeFill)"/>
    </svg>

    <h1 class="greeting">
      Happy Holidays<br>
      And all the best<br>
      to you in the year to come!
    </h1>

    <footer class="brand">
      <span class="brand-name">NEXORA</span>
      <span class="brand-tagline">IT Consulting and Services</span>
    </footer>
  </main>
</body>
</html>
```